Body therapist needs a business card

I need a card for my business which is teaching trainings in body therapy, the company is called Wexcombe Educational Group. I teach to massage therapists around Australia, South East Asia and the USA. I am attaching my logo which will guide you as to what colours I would like to have you consider. Please consult my website to find out more about what I do. www.corvantela.com.au

My name is Daniel Wexcombe. My phone number is (03) 9417 2608 or 0461753208. email is info@corvantela.com.au

```html
<!DOCTYPE html>
<html lang="en">
<head>
<meta charset="utf-8">
<title>Wexcombe Educational Group – Business Card</title>
<link rel="stylesheet" href="https://fonts.googleapis.com/css2?family=Open+Sans:wght@300;400&family=Roboto:wght@400;700&display=swap">
<style>
  :root {
    --backdrop: #d9d9d9;
    --brown: #5e3422;
    --white: #ffffff;
    --red: #b01e24;
    --text-brown: #7a2a22;
    --shadow: rgba(0, 0, 0, 0.25);
  }
  html, body {
    margin: 0;
    padding: 0;
    width: 1200px;
    height: 901px;
    overflow: hidden;
    background: var(--backdrop);
  }
  .canvas {
    width: 1200px;
    height: 901px;
    display: flex;
    flex-direction: column;
    align-items: center;
    justify-content: center;
    gap: 56px;
  }
  .card {
    position: relative;
    width: 620px;
    height: 354px;
    overflow: hidden;
    box-shadow: 0 6px 18px var(--shadow);
  }

  /* Front */
  .card--front {
    background: var(--brown);
    display: flex;
    align-items: center;
    justify-content: center;
  }
  .brand {
    display: flex;
    align-items: center;
    gap: 22px;
  }
  .brand__dot {
    width: 74px;
    height: 74px;
    border-radius: 50%;
    background: var(--white);
    flex: none;
  }
  .brand__name {
    font-family: "Open Sans", sans-serif;
    font-weight: 300;
    color: var(--white);
    font-size: 34px;
    line-height: 1.15;
    letter-spacing: 0.5px;
  }
  .brand__name small {
    display: block;
    font-size: 17px;
    letter-spacing: 0.3px;
  }

  /* Back */
  .card--back {
    background: var(--white);
  }
  .back-accent {
    position: absolute;
    right: -90px;
    top: -30px;
    width: 400px;
    height: 400px;
    border-radius: 50%;
    background: var(--brown);
  }
  .contact {
    position: absolute;
    left: 40px;
    bottom: 34px;
    font-family: "Roboto", sans-serif;
    color: var(--text-brown);
  }
  .contact__name {
    margin: 0 0 8px;
    font-weight: 700;
    font-size: 22px;
    color: var(--red);
  }
  .contact__address {
    margin: 0 0 14px;
    font-size: 14.5px;
    line-height: 1.3;
  }
  .contact__list {
    list-style: none;
    margin: 0;
    padding: 0;
    font-size: 14.5px;
    line-height: 1.55;
  }
  .contact__list li {
    display: flex;
    align-items: center;
    gap: 10px;
  }
  .contact__icon {
    width: 13px;
    height: 13px;
    fill: var(--red);
    flex: none;
  }
</style>
</head>
<body>
  <main class="canvas">
    <section class="card card--front" aria-label="Card front">
      <div class="brand">
        <span class="brand__dot"></span>
        <div class="brand__name">Wexcombe<small>Educational Group</small></div>
      </div>
    </section>

    <section class="card card--back" aria-label="Card back">
      <div class="back-accent"></div>
      <div class="contact">
        <h1 class="contact__name">Daniel Wexcombe</h1>
        <p class="contact__address">P.O. Box 2847, Lindfield East<br>Australia, Victoria, 3158</p>
        <ul class="contact__list">
          <li>
            <svg class="contact__icon" viewBox="0 0 16 16" aria-hidden="true"><path d="M3.6 1.2l2.3 2.6-1.3 1.8c.9 2 2.6 3.7 4.6 4.6l1.8-1.3 2.6 2.3-1.4 2.4C6.9 13.4 2.6 9.1 1.2 3.8z"/></svg>
            <span>(03) 9417 2608</span>
          </li>
          <li>
            <svg class="contact__icon" viewBox="0 0 16 16" aria-hidden="true"><path d="M1 3h14v1.2L8 9 1 4.2z M1 5.8l7 4.8 7-4.8V13H1z"/></svg>
            <span>info@corvantela.com.au</span>
          </li>
          <li>
            <svg class="contact__icon" viewBox="0 0 16 16" aria-hidden="true"><path d="M8 1a7 7 0 1 0 0 14A7 7 0 0 0 8 1zm0 2.5a4.5 4.5 0 1 1 0 9 4.5 4.5 0 0 1 0-9z"/><circle cx="8" cy="8" r="2"/></svg>
            <span>www.corvantela.com.au</span>
          </li>
        </ul>
      </div>
    </section>
  </main>
</body>
</html>
```